Baby Shower Invitation for Vectored Image Provided

Caroline & Desmond's Baby Shower - Black/White/Gold Colors preferred
Please use the vectored portrait image attached. I'd like us on the lower right side of the invitation.
Can be horizontal or vertical layout.
The second image attached has the information needed for you to complete.
I don't want that style copied, it is just an example.

```html
<!DOCTYPE html>
<html lang="en">
<head>
<meta charset="utf-8">
<title>Caroline Hollister Baby Shower Invitation</title>
<link rel="stylesheet" href="https://fonts.googleapis.com/css2?family=Arimo:wght@400;700&family=Open+Sans:wght@400&family=Kaushan+Script&display=swap">
<style>
  :root {
    --ink: #0a0a0a;
    --paper: #ffffff;
    --gold: #fbbd13;
    --gold-deep: #e0a200;
    --backdrop: #ffffff;
  }
  * { margin: 0; padding: 0; box-sizing: border-box; }
  html, body { width: 1200px; height: 1000px; overflow: hidden; background: var(--backdrop); }
  .canvas { position: relative; width: 1200px; height: 1000px; }
  .invitation {
    position: absolute; left: 302px; top: 78px; width: 595px; height: 842px;
    background: var(--paper); overflow: hidden; color: var(--ink);
  }
  .stripe-column {
    position: absolute; top: 0; width: 95px; height: 100%;
    background: repeating-linear-gradient(to bottom,
      var(--ink) 0 22px, var(--paper) 22px 45px,
      var(--gold) 45px 67px, var(--paper) 67px 90px);
  }
  .stripe-column--left { left: 0; }
  .stripe-column--right { right: 0; }
  .headline {
    position: absolute; left: 148px; top: 48px; z-index: 2;
    font: 700 60px/1.3 "Arimo", Arial, sans-serif; letter-spacing: 0.5px;
  }
  .portrait {
    position: absolute; left: 172px; top: 186px; width: 256px; height: 240px; z-index: 1;
    background: linear-gradient(160deg, #4a4a4a, #1c1c1c 60%, #2b2b2b);
    border-radius: 60px 60px 0 0;
  }
  .ribbon { position: absolute; left: 128px; top: 398px; width: 350px; height: 86px; z-index: 3; }
  .intro {
    position: absolute; left: 95px; width: 405px; top: 502px; text-align: center;
    font: 400 12px "Arimo", Arial, sans-serif;
  }
  .honoree {
    position: absolute; left: 95px; width: 405px; top: 528px; text-align: center;
    font: 400 30px "Kaushan Script", cursive;
  }
  .details { position: absolute; left: 111px; top: 580px; width: 373px; height: 153px; }
  .details__rule { position: absolute; left: 0; width: 373px; height: 2px; background: var(--ink); }
  .details__divider { position: absolute; left: 194px; top: 0; width: 2px; height: 114px; background: var(--ink); }
  .date-block { position: absolute; left: 0; top: 0; width: 194px; height: 114px; }
  .date-block__month {
    position: absolute; top: 52px; width: 100%; text-align: center;
    font: 400 21px "Open Sans", Arial, sans-serif;
  }
  .date-block__year {
    position: absolute; top: 80px; width: 100%; text-align: center;
    font: 400 20px "Open Sans", Arial, sans-serif;
  }
  .time-venue { position: absolute; left: 216px; top: 25px; font-family: "Arimo", Arial, sans-serif; }
  .time-venue__time { font-size: 14px; margin-bottom: 13px; }
  .time-venue__place { font-size: 12px; line-height: 15px; padding-left: 12px; }
  .rsvp {
    position: absolute; left: 0; width: 373px; top: 123px; text-align: center; white-space: nowrap;
    font: 400 15px "Arimo", Arial, sans-serif;
  }
  .registry {
    position: absolute; left: 95px; width: 405px; top: 742px; text-align: center;
    font: 400 22px "Kaushan Script", cursive;
  }
</style>
</head>
<body>
<div class="canvas">
  <article class="invitation">
    <div class="stripe-column stripe-column--left"></div>
    <div class="stripe-column stripe-column--right"></div>

    <h1 class="headline">BABY<br>SHOWER</h1>

    <div class="portrait" role="img" aria-label="Vector portrait of the expecting couple, he in a black tee, she in a black dress cradling her belly"></div>

    <svg class="ribbon" viewBox="0 0 350 86" aria-label="A little man is on the way!">
      <path d="M0 30 L32 22 L40 62 L14 72 L22 50 Z" fill="var(--gold-deep)"/>
      <path d="M350 30 L318 22 L310 62 L336 72 L328 50 Z" fill="var(--gold-deep)"/>
      <path d="M28 18 Q175 58 322 18 L322 52 Q175 92 28 52 Z" fill="var(--gold)"/>
      <path id="ribbon-line" d="M40 42 Q175 80 310 42" fill="none"/>
      <text font-family="Arimo, Arial, sans-serif" font-weight="700" font-size="15" fill="#0a0a0a" text-anchor="middle">
        <textPath href="#ribbon-line" startOffset="50%">A LITTLE MAN IS ON THE WAY!</textPath>
      </text>
    </svg>

    <p class="intro">Please join us for a Baby Shower honoring</p>
    <p class="honoree">Caroline Hollister</p>

    <section class="details">
      <div class="details__rule" style="top:0"></div>
      <div class="details__divider"></div>
      <div class="date-block">
        <svg width="194" height="50" viewBox="0 0 194 50">
          <path id="day-arc" d="M48 40 Q100 18 152 40" fill="none"/>
          <text font-family="Open Sans, Arial, sans-serif" font-size="15" letter-spacing="1" fill="#0a0a0a" text-anchor="middle">
            <textPath href="#day-arc" startOffset="50%">SATURDAY</textPath>
          </text>
        </svg>
        <p class="date-block__month">SEPT 01</p>
        <p class="date-block__year">2018</p>
        <svg style="position:absolute;left:40px;top:86px" width="120" height="20" viewBox="0 0 120 20">
          <g fill="var(--gold)">
            <rect x="10" y="2" width="22" height="2"/><rect x="5" y="8" width="27" height="2"/><rect x="0" y="14" width="32" height="2"/>
            <rect x="88" y="2" width="22" height="2"/><rect x="88" y="8" width="27" height="2"/><rect x="88" y="14" width="32" height="2"/>
          </g>
        </svg>
      </div>
      <div class="time-venue">
        <p class="time-venue__time">11 :30 AM &nbsp;- 2:30 PM</p>
        <p class="time-venue__place">THE MAPLECREST<br>4127 BELLWOOD<br>ST. RALEIGH, NC</p>
      </div>
      <div class="details__rule" style="top:114px"></div>
      <p class="rsvp">RSVP to Desmond 919-555-0148 by August 20th</p>
      <div class="details__rule" style="top:151px"></div>
    </section>

    <p class="registry">Caroline is registered at Little Nest Baby</p>
  </article>
</div>
</body>
</html>
```